US Recruiting Firm Needs Dynamic Tri-Fold Brochure

Need tri-fold professional brochure for HR recruiting and consulting firm based in the US.

Target Market(s)

Clients seeking administrative and human resources talent

Industry/Entity Type

Recruitment

Font styles to use
Sans Serif

Requirements
Should not have
• No weird shapes
• No heavy geometric shapes -- I prefer curvy lines
• Not a dark brochure

```html
<!DOCTYPE html>
<html lang="en">
<head>
<meta charset="utf-8">
<title>Harbor Office Recruiters – Tri-Fold Brochure</title>
<link href="https://fonts.googleapis.com/css2?family=Didact+Gothic&family=Montserrat:wght@600;700;800&display=swap" rel="stylesheet">
<style>
  :root {
    --purple: #9b1f7e;
    --orange: #f26a21;
    --navy: #1f3157;
    --lime: #9cc83a;
    --panel-grey: #e9e9ea;
    --paper: #ffffff;
    --stage: #f2f2f2;
    --body-text: #2b2b2b;
  }
  * { margin: 0; padding: 0; box-sizing: border-box; }
  html, body { width: 1200px; height: 800px; overflow: hidden; background: var(--stage); }
  .brochure {
    position: absolute; left: 45px; top: 20px;
    width: 1110px; height: 760px;
    display: flex;
    box-shadow: 0 6px 24px rgba(0,0,0,.18);
    overflow: hidden;
  }
  .panel { position: relative; width: 370px; height: 100%; }
  .panel--about { background: var(--paper); }
  .panel--contact, .panel--cover { background: var(--panel-grey); }
  .panel + .panel { border-left: 1px solid rgba(0,0,0,.06); }

  /* About panel */
  .about-title {
    position: absolute; left: 36px; top: 50px;
    font-family: 'Didact Gothic', sans-serif; font-size: 26px;
    color: var(--navy); letter-spacing: 1px;
  }
  .about-title .accent { font-family: 'Montserrat', sans-serif; font-weight: 800; color: var(--orange); }
  .about-rule { position: absolute; left: 34px; top: 86px; }
  .about-copy {
    position: absolute; left: 36px; top: 110px; width: 300px;
    font-family: 'Didact Gothic', sans-serif; font-size: 11.5px;
    line-height: 1.42; color: var(--body-text); text-align: justify;
  }
  .about-copy p + p { margin-top: 12px; }
  .photo-training {
    position: absolute; left: 0; top: 510px; width: 370px; height: 220px;
    background: linear-gradient(160deg, #f4f6f8 0%, #d7dde3 45%, #9aa3ad 100%);
  }

  /* Contact panel */
  .callout { position: absolute; left: 30px; top: 48px; }
  .callout-text {
    position: absolute; left: 30px; top: 66px; width: 310px;
    text-align: center; line-height: 1.15;
  }
  .callout-lead { font-family: 'Montserrat', sans-serif; font-weight: 800; font-size: 26px; color: var(--purple); }
  .callout-sub { font-family: 'Didact Gothic', sans-serif; font-size: 15px; color: var(--navy); }
  .callout-offer { font-family: 'Montserrat', sans-serif; font-weight: 800; font-size: 21px; color: var(--purple); }
  .callout-cta { font-family: 'Didact Gothic', sans-serif; font-size: 15px; color: var(--navy); }
  .callout-cta strong { font-family: 'Montserrat', sans-serif; font-weight: 800; }
  .phone-line {
    position: absolute; left: 0; top: 232px; width: 370px; text-align: center;
    font-family: 'Montserrat', sans-serif; font-weight: 800; font-size: 25px; color: var(--purple);
  }
  .email-line {
    position: absolute; left: 0; top: 270px; width: 370px; text-align: center;
    font-family: 'Didact Gothic', sans-serif; font-size: 16px; color: var(--navy);
  }
  .photo-meeting {
    position: absolute; left: 415px; top: 320px; width: 740px; height: 410px;
    background: linear-gradient(170deg, #f1f3f5 0%, #c9cfd6 40%, #6f7780 75%, #4a4f56 100%);
  }

  /* Cover panel */
  .brand {
    position: absolute; right: 28px; top: 38px;
    display: flex; align-items: center; gap: 10px;
  }
  .brand-dot { width: 30px; height: 30px; border-radius: 50%; background: var(--purple); }
  .brand-name {
    font-family: 'Didact Gothic', sans-serif; font-size: 19px; color: var(--navy);
    line-height: 1.1; letter-spacing: .5px;
  }
  .brand-tag {
    position: absolute; right: 28px; top: 86px;
    font-family: 'Didact Gothic', sans-serif; font-size: 11px; color: var(--navy);
  }
  .cover-headline { position: absolute; left: 0; top: 126px; width: 370px; text-align: center; line-height: 1.2; }
  .cover-kicker { font-family: 'Montserrat', sans-serif; font-weight: 800; font-size: 27px; color: var(--orange); }
  .cover-line { font-family: 'Didact Gothic', sans-serif; font-size: 19px; color: var(--navy); }
  .cover-line--strong { font-family: 'Montserrat', sans-serif; font-weight: 800; font-size: 19px; color: var(--navy); }

  /* Footer band */
  .footer-band { position: absolute; left: 0; bottom: 0; width: 1110px; height: 110px; }
  .footer-url {
    position: absolute; bottom: 22px; width: 370px; text-align: center;
    font-family: 'Didact Gothic', sans-serif; font-size: 17px; color: var(--paper); letter-spacing: .5px;
  }
  .footer-url--about { left: 0; }
  .footer-url--contact { left: 370px; }
  .footer-url--cover { left: 740px; }
</style>
</head>
<body>
<main class="brochure">
  <section class="panel panel--about">
    <h2 class="about-title">ABOUT <span class="accent">US</span></h2>
    <svg class="about-rule" width="290" height="14" viewBox="0 0 290 14">
      <path d="M2 12 Q 140 2 288 4" fill="none" stroke="var(--purple)" stroke-width="2.5"/>
    </svg>
    <div class="about-copy">
      <p>Harbor Office Recruiters is a recruiting and search firm that specializes in providing top-notch administrative, professional, and executive level human resources talent. We provide best-in-class talent to companies seeking to simplify their recruiting process, increase efficiency, and optimize productivity. Each search is customized based on our clients' requirements. We provide quality, timely, and efficient services. Our recruiters are highly skilled in identifying, screening, interviewing, and assessing candidates across various industries. We develop a partnership with our client and candidate in order to make the recruitment process a success for both parties.</p>
      <p>At Harbor Office Recruiters, competence + talent emerge. We are experienced human resources professionals exclusively dedicated to recruiting and placing human resources professionals. We do we love and know for sure: human resources recruiting and consulting. We help awesome companies attract and retain the best employees, increase their profits, and optimize productivity.</p>
    </div>
    <div class="photo-training" role="img" aria-label="Photo: a presenter at a whiteboard leading a training session for seated professionals"></div>
  </section>

  <section class="panel panel--contact">
    <svg class="callout" width="310" height="170" viewBox="0 0 310 170">
      <path d="M6 6 H304 V140 H190 L170 164 L160 140 H6 Z" fill="none" stroke="var(--orange)" stroke-width="2"/>
    </svg>
    <div class="callout-text">
      <div class="callout-lead">TO LEARN MORE</div>
      <div class="callout-sub">AND REQUEST A</div>
      <div class="callout-offer">FREE CONSULTATION</div>
      <div class="callout-cta">CONTACT US <strong>TODAY</strong></div>
    </div>
    <div class="phone-line">CALL - 555 010 2030</div>
    <div class="email-line">info@harborofficerecruiters.com</div>
  </section>

  <section class="panel panel--cover">
    <div class="brand">
      <span class="brand-dot"></span>
      <span class="brand-name">HARBOR OFFICE<br>RECRUITERS</span>
    </div>
    <div class="brand-tag">Human Resources Staffing &amp; Consulting</div>
    <div class="cover-headline">
      <div class="cover-kicker">SPECIALIZING IN</div>
      <div class="cover-line">ADMINISTRATIVE,</div>
      <div class="cover-line">PROFESSIONAL, AND</div>
      <div class="cover-line--strong">EXECUTIVE HR TALENT</div>
    </div>
  </section>

  <div class="photo-meeting" role="img" aria-label="Photo: smiling business professionals shaking hands across a meeting table"></div>

  <svg class="footer-band" viewBox="0 0 1110 110" preserveAspectRatio="none">
    <path d="M0 42 Q185 22 370 10 V110 H0 Z" fill="var(--purple)"/>
    <path d="M0 42 Q185 22 370 10" fill="none" stroke="var(--lime)" stroke-width="3"/>
    <path d="M370 42 Q555 22 740 10 V110 H370 Z" fill="var(--purple)"/>
    <path d="M370 42 Q555 22 740 10" fill="none" stroke="var(--lime)" stroke-width="3"/>
    <path d="M740 42 Q925 22 1110 10 V110 H740 Z" fill="var(--purple)"/>
    <path d="M740 42 Q925 22 1110 10" fill="none" stroke="var(--lime)" stroke-width="3"/>
  </svg>
  <div class="footer-url footer-url--about">www.harborofficerecruiters.com</div>
  <div class="footer-url footer-url--contact">www.harborofficerecruiters.com</div>
  <div class="footer-url footer-url--cover">www.harborofficerecruiters.com</div>
</main>
</body>
</html>
```